Logo and Business Card Design for Innovative Corporate Law Firm

Varlo Advogados is a new, young and innovative law firm focused in corporate law, mainly helping start-ups in the incorporation process, liasing with strategic investors, funds, private equity and venture/seed capital businesses around the world.

We need a logo and business card design that correctly captures our modern and savvy, yet sober, approach to legal practice.

We are looking to starting with the logo and business card designs and further ahead move on to stationery, website etc.

We are located in São Paulo/Brazil, but we expect our logo and stationery design to be able to reach and connect to possible clients worldwide due to the international characteristic of our practice.

Be creative! We have no restrictions on colors, one-sided or two-sided cards, logos, font styles...
Updates

Guys, just to be clear: The project shall contemplate a full stationery design, but the logo and business card may be proposed in advance due to our urgent need to have these cards ready for our clients. The other stationery items may be proposed later on. Many thanks!

Dear all, please be aware that the logo should look good both in collor and black and white. 

Thanks

Industry/Entity Type

Business

Requirements
Must have
• Modern but sober approach
Nice to have
• I tend to like grey collor schemes with red touches, but this is not a must have...
Should not have
• Excessively bright, shiny look, that will make our legal services look too commercial. No excesses.

```html
<!DOCTYPE html>
<html lang="pt-BR">
<head>
<meta charset="utf-8">
<title>Varlo Advogados – Business Card</title>
<link href="https://fonts.googleapis.com/css2?family=Oswald:wght@400;600&family=Open+Sans:wght@400;600&display=swap" rel="stylesheet">
<style>
  :root {
    --page-bg: #e9eaec;
    --brand-blue: #1f74c4;
    --brand-blue-deep: #1663ad;
    --edge-grey: #d9dbde;
    --edge-grey-light: #eef0f2;
    --card-white: #ffffff;
    --ink: #3a3d42;
    --ink-soft: #6b7078;
    --mark-grey: #c7cacf;
  }
  * { margin: 0; padding: 0; box-sizing: border-box; }
  html, body { width: 1200px; height: 1023px; overflow: hidden; }
  body {
    background: var(--page-bg);
    display: flex;
    flex-direction: column;
    align-items: center;
    justify-content: center;
    gap: 36px;
    font-family: "Open Sans", Arial, sans-serif;
  }
  .card {
    position: relative;
    width: 820px;
    height: 456px;
    overflow: hidden;
    box-shadow: 0 10px 28px rgba(0,0,0,.18);
  }

  /* Front */
  .card-front {
    background: linear-gradient(135deg, var(--brand-blue) 0%, var(--brand-blue-deep) 100%);
  }
  .card-front .edge-band {
    position: absolute; top: 0; right: 0; bottom: 0; width: 44px;
    background: linear-gradient(90deg, var(--edge-grey) 0%, var(--edge-grey-light) 100%);
  }
  .card-front .faint-disc {
    position: absolute; left: -120px; bottom: -260px;
    width: 520px; height: 520px; border-radius: 50%;
    background: rgba(255,255,255,.08);
  }
  .brand {
    position: absolute; left: 190px; top: 170px;
    display: flex; align-items: center; gap: 22px;
  }
  .brand-dot {
    width: 64px; height: 64px; border-radius: 50%;
    background: var(--mark-grey);
  }
  .brand-text { display: flex; flex-direction: column; }
  .brand-name {
    font-family: "Oswald", "Arial Narrow", sans-serif;
    font-weight: 600; font-size: 58px; line-height: 1;
    letter-spacing: 2px; text-transform: uppercase;
    color: var(--card-white);
  }
  .brand-web {
    font-family: "Oswald", "Arial Narrow", sans-serif;
    font-weight: 400; font-size: 15px; letter-spacing: 1.5px;
    text-transform: uppercase; color: rgba(255,255,255,.85);
    margin-top: 8px; text-align: right;
  }

  /* Back */
  .card-back { background: var(--card-white); }
  .card-back .edge-band {
    position: absolute; top: 0; left: 0; bottom: 0; width: 36px;
    background: var(--brand-blue);
  }
  .card-back .faint-disc {
    position: absolute; right: -140px; bottom: -280px;
    width: 540px; height: 540px; border-radius: 50%;
    background: rgba(150,155,162,.14);
  }
  .contact {
    position: absolute; left: 90px; top: 70px;
    list-style: none; color: var(--ink);
    font-size: 17px; line-height: 1.45;
  }
  .contact .address { margin-bottom: 18px; color: var(--ink-soft); }
  .contact-line { display: flex; align-items: center; gap: 12px; margin-bottom: 6px; }
  .contact-line svg { width: 18px; height: 18px; flex: none; }
  .icon { fill: none; stroke: var(--brand-blue); stroke-width: 1.8; }
</style>
</head>
<body>

  <section class="card card-front" aria-label="Card front">
    <div class="faint-disc"></div>
    <div class="brand">
      <div class="brand-dot"></div>
      <div class="brand-text">
        <span class="brand-name">Varlo Advogados</span>
        <span class="brand-web">www.varloadvogados.com.br</span>
      </div>
    </div>
    <div class="edge-band"></div>
  </section>

  <section class="card card-back" aria-label="Card back">
    <div class="edge-band"></div>
    <div class="faint-disc"></div>
    <ul class="contact">
      <li class="address">Rua Augusta, 1200 – Sala 84<br>São Paulo – SP 01304-001</li>
      <li class="contact-line">
        <svg viewBox="0 0 20 20" aria-hidden="true"><path class="icon" d="M5 2h3l1.5 4-2 1.5a10 10 0 0 0 5 5l1.5-2 4 1.5v3a2 2 0 0 1-2 2A15 15 0 0 1 3 4a2 2 0 0 1 2-2z"/></svg>
        <span>+55 11 3456 7890</span>
      </li>
      <li class="contact-line">
        <svg viewBox="0 0 20 20" aria-hidden="true"><rect class="icon" x="2" y="4" width="16" height="12" rx="1"/><path class="icon" d="M2 5l8 6 8-6"/></svg>
        <span>rvarlo@varloadvogados.com.br</span>
      </li>
      <li class="contact-line">
        <svg viewBox="0 0 20 20" aria-hidden="true"><circle class="icon" cx="10" cy="10" r="8"/><path class="icon" d="M2 10h16M10 2c3 3 3 13 0 16M10 2c-3 3-3 13 0 16"/></svg>
        <span>www.varloadvogados.com.br</span>
      </li>
    </ul>
  </section>

</body>
</html>
```